依頼詳細
作りたいチラシのイメージは、「参考画像.jpg」の通りです。

裏面のデザイン(価格表)は完成しておりますので、デザインの雰囲気をなるべく合わせていただけると幸いです。(「裏面画像.jpg」)
また、以前に表面のデザインも作成しておりますので、こちらも参考にしてください。(「表面画像.jpg」)

特に、
・往診料無料
・ワクチン料金
・フィラリア症予防薬料金
・自宅で手軽に予防ができる
上記の内容をより訴求できるデザインにしたいと思っております。

動物病院ですので、優しく、特に女性受けが良さそうなイメージで作成をお願いいたします。

使用する色は、主に「緑、オレンジ」をメインに考えておりますが、色の具合は自由に調節いただいて結構です。
作りたいチラシのイメージは、「参考画像.jpg」の通りですが、デザインは自由に調節していただいて結構です。
また、こちらで用意させていただく素材以外で、デザインに沿った文言・イラスト・アイコン・写真などがありましたら、自由に取り入れていただければと思います。
記載項目
・チラシに使用する文章はこちらで用意いたします。

「参考画像.jpg」の①~⑩にはPDFファイル(チラシ記載内容.pdf)に記載されている文章を使用してください。

・院長の画像については、画像1、画像2のいずれかをお使いください。
※psd形式以外のデータをご希望の際はお申し付けください。

・ロゴについては画像3をお使いください。
サイズ
A4
ページ数
片面
希望イメージ
• +5 0 +5
• シンプル
複雑
• 単色
カラフル
• 暗い
明るい
• 日常
高級
• 遊び心
厳粛
• 未来的
伝統的
• 女性的
男性的
希望する色
納品ファイル
• 高解像度JPG (.jpg)
• イラストレーター形式 (.ai)
補足説明
依頼公開後の追記内容
■ 選んだ理由

全体的なイメージと、特に家のデザインが気に入りました。

■ 提案者全員のお礼・コメント

この度はご提案くださり誠にありがとうございました。
どれも良いものばかりで、選択に非常に迷いました。

また機会がございましたら、その時はどうぞよろしくお願いいたします。

```html
<!DOCTYPE html>
<html lang="ja">
<head>
<meta charset="utf-8">
<title>ひなた動物病院 往診チラシ</title>
<link href="https://fonts.googleapis.com/css2?family=M+PLUS+Rounded+1c:wght@500;700;800;900&display=swap" rel="stylesheet">
<style>
:root{
  --green:#3d9a34;
  --green-dark:#23761f;
  --green-pale:#eaf5e2;
  --orange:#f08519;
  --orange-pale:#fff1de;
  --yellow:#fff3a8;
  --cream:#fffbea;
  --red:#e2382b;
  --ink:#333;
  --white:#fff;
}
*{box-sizing:border-box;margin:0;padding:0}
html,body{width:846px;height:1200px;overflow:hidden}
body{font-family:"M PLUS Rounded 1c",sans-serif;color:var(--ink);background:var(--cream);position:relative}
.flyer{position:relative;width:846px;height:1200px;overflow:hidden;background:var(--cream)}

.headline{position:absolute;left:0;top:0;width:846px;height:112px;background:var(--white);border-bottom:6px solid var(--green);display:flex;align-items:center;justify-content:center}
.headline h1{font-size:50px;font-weight:900;color:var(--green-dark);letter-spacing:1px;white-space:nowrap;background:linear-gradient(transparent 62%,var(--yellow) 62%)}

.director-photo{position:absolute;left:18px;top:126px;width:320px;height:292px;border-radius:14px;background:linear-gradient(160deg,#f3efe6,#d9d2c2 60%,#b9b0a0)}
.director-name{position:absolute;left:110px;top:378px;font-size:18px;font-weight:700;background:var(--white);padding:3px 12px;border-radius:12px;white-space:nowrap}
.director-name b{font-size:22px;margin-left:6px}

.points{position:absolute;left:356px;top:132px;width:480px}
.points li{list-style:none;font-size:38px;font-weight:900;color:var(--green);margin-bottom:14px;white-space:nowrap;line-height:1.2}
.call-out{position:absolute;left:262px;top:262px;font-size:24px;font-weight:800;color:var(--orange);line-height:1.3;transform:rotate(-4deg);white-space:nowrap}
.free-visit{position:absolute;left:560px;top:290px;width:270px;padding:10px 8px;background:var(--white);border:4px solid var(--red);border-radius:14px;text-align:center;color:var(--red);font-weight:900;font-size:24px;line-height:1.35;white-space:nowrap}
.free-visit em{font-style:normal;font-size:32px;background:var(--yellow);padding:0 4px}

.price{position:absolute;top:428px;height:212px;background:var(--white);border:3px solid var(--orange);border-radius:10px;overflow:hidden}
.price h2{height:30px;background:var(--orange);color:var(--white);font-size:19px;font-weight:800;text-align:center;line-height:30px}
.price table{width:100%;border-collapse:collapse}
.price td,.price th{border-bottom:1px dashed #f3c08a;font-weight:700;white-space:nowrap}
.vaccine{left:14px;width:408px}
.vaccine .species{width:80px;background:var(--green);color:var(--white);font-size:26px;text-align:center;border-bottom:2px solid var(--white)}
.vaccine td{height:35.6px;font-size:18px;padding-left:10px}
.vaccine .yen{text-align:right;padding-right:12px;color:var(--red);font-size:21px}
.filaria{left:430px;width:402px}
.filaria th{height:26px;font-size:13px;background:var(--orange-pale);color:var(--orange)}
.filaria td{height:25.6px;font-size:16px;text-align:center}
.filaria td.weight{background:var(--green-pale);color:var(--green-dark);text-align:left;padding-left:10px}
.filaria td.yen{color:var(--red);font-size:18px}

.schedule{position:absolute;left:14px;top:648px;width:818px;border:3px solid var(--green);border-radius:10px;overflow:hidden;background:var(--white)}
.schedule table{width:100%;border-collapse:collapse}
.schedule th{height:30px;background:var(--green);color:var(--white);font-size:18px;font-weight:800}
.schedule td{height:41px;border-bottom:1px solid #cfe5c6;font-size:13px;font-weight:700;padding:0 8px;line-height:1.35}
.schedule td.pref{width:110px;background:var(--green-pale);color:var(--green-dark);font-size:20px;font-weight:900;text-align:center}
.schedule td.dates{width:330px;border-right:1px dashed #b9d9ad}
.schedule td.all{text-align:center;font-size:20px;color:var(--green-dark)}
.schedule tr:last-child td{border-bottom:none}
.note{position:absolute;left:20px;top:898px;font-size:12px;font-weight:700;color:#666}

.contact{position:absolute;left:0;top:920px;width:846px;height:280px;background:var(--white);border-top:6px solid var(--orange)}
.contact h2{position:absolute;left:24px;top:14px;font-size:36px;font-weight:900;color:var(--orange);white-space:nowrap}
.hours{position:absolute;right:22px;top:12px;width:150px;border:3px solid var(--green);border-radius:10px;text-align:center;overflow:hidden}
.hours span{display:block;background:var(--green);color:var(--white);font-size:15px;font-weight:800;padding:2px 0}
.hours b{display:block;font-size:20px;color:var(--green-dark);padding:4px 0}
.phone{position:absolute;left:24px;top:78px;display:flex;align-items:center;gap:8px;font-size:50px;font-weight:900;color:var(--green-dark);white-space:nowrap}
.mail{position:absolute;left:470px;top:96px;display:flex;align-items:center;gap:8px;font-size:25px;font-weight:800;color:var(--green-dark);white-space:nowrap}
.footer{position:absolute;left:0;top:170px;width:846px;height:110px;background:var(--green);display:flex;align-items:center;padding:0 24px;gap:24px;color:var(--white)}
.brand{display:flex;align-items:center;gap:12px;font-size:36px;font-weight:900;white-space:nowrap}
.brand i{display:block;width:40px;height:40px;border-radius:50%;background:var(--white)}
.address{font-size:18px;font-weight:700;line-height:1.5}
</style>
</head>
<body>
<div class="flyer">
  <header class="headline"><h1>「ワクチンはおウチで」が新しい!</h1></header>

  <div class="director-photo" role="img" aria-label="笑顔の院長の写真"></div>
  <p class="director-name">院長<b>森本 誠</b></p>

  <ul class="points">
    <li>・自宅でワクチン</li>
    <li>・自宅でフィラリア予防</li>
  </ul>
  <p class="call-out">お気軽に<br>ご連絡ください!</p>
  <p class="free-visit">往診料<em>無料</em>で<br>お伺いします!</p>

  <section class="price vaccine">
    <h2>ワクチン料金表</h2>
    <table>
      <tr><th class="species" rowspan="3">犬用</th><td>・狂犬病ワクチン</td><td class="yen">2,500円</td></tr>
      <tr><td>・5種混合ワクチン</td><td class="yen">4,500円</td></tr>
      <tr><td>・8種混合ワクチン</td><td class="yen">5,000円</td></tr>
      <tr><th class="species" rowspan="2">猫用</th><td>・3種混合ワクチン</td><td class="yen">4,000円</td></tr>
      <tr><td>・5種混合ワクチン</td><td class="yen">5,000円</td></tr>
    </table>
  </section>

  <section class="price filaria">
    <h2>フィラリア症予防薬料金表</h2>
    <table>
      <tr><th></th><th>1回分</th><th>1回分お得な6回分セット</th></tr>
      <tr><td class="weight">~5kgまで</td><td class="yen">600円</td><td class="yen">3,000円</td></tr>
      <tr><td class="weight">5kg~10kg</td><td class="yen">700円</td><td class="yen">4,900円</td></tr>
      <tr><td class="weight">10kg~20kg</td><td class="yen">900円</td><td class="yen">6,300円</td></tr>
      <tr><td class="weight">20kg~30kg</td><td class="yen">1,100円</td><td class="yen">7,700円</td></tr>
      <tr><td class="weight">30kg~40kg</td><td class="yen">1,200円</td><td class="yen">9,000円</td></tr>
      <tr><td class="weight">40kg以上</td><td class="yen">1,500円</td><td class="yen">10,500円</td></tr>
    </table>
  </section>

  <section class="schedule">
    <table>
      <tr><th colspan="2">往診スケジュール</th><th>往診地域</th></tr>
      <tr><td class="pref">栃木県</td><td class="dates">4/1(水)、4/24(金)、5/8(金)、5/22(金)<br>5/11(月)、5/15(金)、5/29(金)</td><td>足利市、佐野市、栃木市、小山市、鹿沼市<br>宇都宮市、真岡市、下野市、壬生町 ほか</td></tr>
      <tr><td class="pref">群馬県</td><td class="dates">4/2(木)、4/16(木)、4/30(木)<br>5/14(木)、5/28(木)</td><td>太田市、館林市、桐生市、みどり市<br>伊勢崎市、大泉町、邑楽町 ほか</td></tr>
      <tr><td class="pref">埼玉県</td><td class="dates">4/6(月)、4/13(月)、4/17(金)<br>5/4(月)、5/18(月)</td><td class="all">全域</td></tr>
      <tr><td class="pref">東京都</td><td class="dates">4/7(火)、4/21(火)、5/5(火)<br>5/12(火)、5/26(火)</td><td class="all">全域</td></tr>
      <tr><td class="pref">神奈川県</td><td class="dates">4/8(水)、4/22(水)<br>5/6(水)、5/20(水)</td><td>川崎市、横浜市、相模原市、大和市<br>町田市周辺 ほか</td></tr>
    </table>
  </section>
  <p class="note">※上記以外の日程・地域をご希望の場合もお気軽にご相談ください。</p>

  <section class="contact">
    <h2>往診のご予約・ご相談はこちら</h2>
    <div class="hours"><span>受付時間</span><b>9:00~21:00</b></div>
    <p class="phone">
      <svg width="48" height="48" viewBox="0 0 48 48" aria-hidden="true"><circle cx="24" cy="24" r="24" fill="#f08519"/><path d="M17 12c2 0 4 5 4 6s-3 2-3 3c1 4 5 8 9 9 1 0 2-3 3-3s6 2 6 4-3 5-5 5C21 36 12 27 12 17c0-2 3-5 5-5z" fill="#fff"/></svg>
      080-1234-5678
    </p>
    <p class="mail">
      <svg width="34" height="26" viewBox="0 0 34 26" aria-hidden="true"><rect x="1" y="1" width="32" height="24" rx="3" fill="#f08519"/><path d="M3 4l14 11L31 4" stroke="#fff" stroke-width="2.5" fill="none"/></svg>
      info@hinata-vet.jp
    </p>
    <div class="footer">
      <div class="brand"><i></i>ひなた動物病院</div>
      <p class="address">〒320-0000 栃木県足利市緑町 1-2-3<br>TEL 0284-00-0000</p>
    </div>
  </section>
</div>
</body>
</html>
```